Business Card Design Project

We need a business card design for a company based in San Diego California named "TLKMasonry Inc." We are dedicated installers of fireplaces, pre cast concrete, stone masonry. We also pecialice in block construction.

Thank you very much guys, very good designs so far although I would like to point out that the front should have: Company name, license number, and please tell me if a Qr code is too much (if it isn't then it should be in a bottom corner. <img src="http://qr.vendrixcodes.example/?l=1&s=8&d=BEGIN:VCARD%0AVERSION:2.1%0AN:Lopez;Arturo+%0AFN:Arturo++Lopez%0ATEL;WORK;VOICE:15559301846%0AEMAIL;WORK;INTERNET:tlkmasonry%40mailbrook.example%0AURL:www.tlkmasonry.example%0AORG:TLK+Masonry+Inc%0ATITLE:Contractor%0AADR;WORK:;;;Oceanside;California;40317;USA%0AEND:VCARD" alt="QRCode"/>  Or I'll upload the picture.

Also we are currently constructing our website, there you can find pictures of what we do. 
tlkmasonry.example 
Thank you guys again.

• Company name: T L K Masonry Inc
Licence number: 482913
Arturo Lopez Vega
Phone number: 4820 391 2754
• We would like to have an image that represents the business area of work; a fireplace, a fountain, a balcony, a niche, an arch.

```html
<!DOCTYPE html>
<html lang="en">
<head>
<meta charset="utf-8">
<title>TLK Masonry Inc – Business Card</title>
<link rel="stylesheet" href="https://fonts.googleapis.com/css2?family=Jost:wght@400;500;600&display=swap">
<style>
  :root {
    --card-bg: #ffffff;
    --card-border: #6b6b6b;
    --stone-pale: #e4e4e4;
    --stone-mid: #b9b9b9;
    --stone-deep: #8e8e8e;
    --title-fill: #ffffff;
    --title-shadow: rgba(30, 30, 30, 0.7);
    --contact-ink: #262626;
  }
  html, body {
    margin: 0;
    padding: 0;
    width: 1200px;
    height: 686px;
    overflow: hidden;
    background: var(--card-bg);
  }
  .card {
    position: relative;
    width: 1200px;
    height: 686px;
    box-sizing: border-box;
    border: 2px solid var(--card-border);
    background: var(--card-bg);
    overflow: hidden;
    font-family: "Jost", "Futura", sans-serif;
  }
  .card__photo {
    position: absolute;
    inset: 0;
    width: 100%;
    height: 100%;
  }
  .brand {
    margin: 0;
    font-weight: 400;
    color: var(--title-fill);
    text-shadow: 8px 10px 10px var(--title-shadow);
  }
  .brand__initials {
    position: absolute;
    left: 64px;
    top: 36px;
    font-size: 272px;
    line-height: 272px;
    letter-spacing: 22px;
    white-space: nowrap;
  }
  .brand__name {
    position: absolute;
    left: 80px;
    top: 318px;
    font-size: 84px;
    line-height: 84px;
    font-weight: 500;
    letter-spacing: 0;
    white-space: nowrap;
  }
  .contact {
    position: absolute;
    right: 86px;
    top: 470px;
    text-align: right;
    color: var(--contact-ink);
  }
  .contact__name {
    margin: 0 0 4px;
    font-size: 29px;
    line-height: 40px;
    font-weight: 600;
    font-variant: small-caps;
    letter-spacing: 1px;
  }
  .contact__line {
    margin: 0 0 4px;
    font-size: 29px;
    line-height: 40px;
    font-weight: 400;
  }
</style>
</head>
<body>
  <div class="card">
    <svg class="card__photo" viewBox="0 0 1200 686" role="img" aria-label="Grayscale photograph of a carved stone fireplace mantel with columns">
      <defs>
        <linearGradient id="stoneTone" x1="0" y1="0" x2="1" y2="0.35">
          <stop offset="0" stop-color="#ffffff"/>
          <stop offset="0.22" stop-color="#f2f2f2"/>
          <stop offset="0.4" stop-color="var(--stone-pale)"/>
          <stop offset="0.7" stop-color="var(--stone-mid)"/>
          <stop offset="1" stop-color="var(--stone-deep)"/>
        </linearGradient>
      </defs>
      <rect width="1200" height="686" fill="url(#stoneTone)"/>
    </svg>

    <h1 class="brand">
      <span class="brand__initials">T L K</span>
      <span class="brand__name">MASONRY INC</span>
    </h1>

    <div class="contact">
      <p class="contact__name">Arturo Lopez Vega</p>
      <p class="contact__line">ph: 4820 391 2754</p>
      <p class="contact__line">license number: 482913</p>
    </div>
  </div>
</body>
</html>
```